Travelogue book cover

The book is a collection of stories from my travels around the world. These stories run a full range of emotions from unbridled joy, to things that are much funnier today than they were at the time, to moments of sadness while reflecting on places that have been irrevocably changed. This world is an amazing and powerful place, and my stories tell its tale. The overall vibe is to love exploring the world, the thrill of discovery, the comedy of getting outside of your comfort zone, and just generally wanting to convey a sense of wonder and make people feel like they want to get out and explore for themselves.

The audience is in the 30-50 age target, educated, all genders, and either an experienced traveller or wishes they were.

On the style, I am looking for something that stands out when a reader is browsing Brellowmart. Since most book covers are bright, full bleed and busy, I would prefer something that emphasizes white space and simplicity.

```html
<!DOCTYPE html>
<html lang="en">
<head>
<meta charset="UTF-8">
<title>Travelogue — Book Cover</title>
<link href="https://fonts.googleapis.com/css2?family=Montserrat:wght@700&family=Lora:wght@400&display=swap" rel="stylesheet">
<style>
  :root {
    --cover-bg: #3a1f2a;
    --title-orange: #c8633a;
    --author-green: #4a7a62;
    --art-teal: #4fc4ad;
    --art-cream: #f3edc0;
    --art-coral: #e07a55;
    --art-deep: #2b8f8a;
    --art-sun: #f0c77a;
  }
  html, body {
    margin: 0;
    padding: 0;
    width: 675px;
    height: 1200px;
    overflow: hidden;
    background: var(--cover-bg);
  }
  .cover {
    position: relative;
    width: 675px;
    height: 1200px;
    background: var(--cover-bg);
  }
  .cover__title {
    position: absolute;
    top: 189px;
    left: 0;
    width: 675px;
    margin: 0;
    text-align: center;
    font-family: "Montserrat", sans-serif;
    font-weight: 700;
    font-size: 34px;
    letter-spacing: 7.3px;
    text-indent: 7.3px;
    color: var(--title-orange);
    line-height: 1;
  }
  .cover__author {
    position: absolute;
    top: 246px;
    left: 0;
    width: 675px;
    margin: 0;
    text-align: center;
    font-family: "Lora", serif;
    font-weight: 400;
    font-size: 28.5px;
    color: var(--author-green);
    line-height: 1;
  }
  .cover__art {
    position: absolute;
    left: 73px;
    top: 457px;
    width: 534px;
    height: 660px;
  }
</style>
</head>
<body>
  <main class="cover">
    <h1 class="cover__title">TRAVELOGUE</h1>
    <p class="cover__author">Autor Name</p>
    <svg class="cover__art" viewBox="0 0 534 660" role="img"
         aria-label="Illustration: a backpacker standing inside an open suitcase frame looking out at a glowing world map, surrounded by clouds, leafy plants, city towers, a small globe and luggage, above rippling water">
      <defs>
        <radialGradient id="artGlow" cx="50%" cy="50%" r="52%">
          <stop offset="0%" stop-color="var(--art-cream)"/>
          <stop offset="30%" stop-color="var(--art-teal)"/>
          <stop offset="58%" stop-color="var(--art-deep)"/>
          <stop offset="78%" stop-color="var(--art-coral)"/>
          <stop offset="90%" stop-color="var(--art-sun)" stop-opacity="0.5"/>
          <stop offset="100%" stop-color="var(--cover-bg)" stop-opacity="0"/>
        </radialGradient>
      </defs>
      <rect x="0" y="0" width="534" height="660" fill="url(#artGlow)"/>
    </svg>
  </main>
</body>
</html>
```